Law Firm Website

We are looking to update our old, tired and very flat website. We have someone who will code and host the site but we need some design inspiration. The website will consist of no more than 2/3 pages, possibly with pop-ups for information. We already have all the blurb. We would like something distinctive, clean and eye-catching, using the purple and white theme that we already use on our firm stationery. Examples uploaded. Current website URL is www.dunmorewillett.example.

Industry/Entity Type

Law Firm

```html
<!DOCTYPE html>
<html lang="en">
<head>
<meta charset="utf-8">
<title>Dunmore Willett Solicitors – Areas of Expertise</title>
<link href="https://fonts.googleapis.com/css2?family=Mulish:wght@400;500;600;700&display=swap" rel="stylesheet">
<style>
  :root{
    --purple-dark:#3a2452;
    --purple:#432a5e;
    --purple-text:#5a3a7e;
    --gold:#d4b66a;
    --gold-soft:#e3cb8c;
    --ink:#1c1c1c;
    --grey:#777;
    --grey-light:#e4e4e4;
    --white:#fff;
  }
  *{box-sizing:border-box;margin:0;padding:0}
  html,body{width:1200px;height:1200px;overflow:hidden;background:var(--white);font-family:'Mulish',sans-serif;color:var(--ink)}
  .page{position:relative;width:1200px;height:1200px}

  .site-header{position:absolute;left:0;top:0;width:1200px;height:153px;
    background:linear-gradient(180deg,#553a72 0,#553a72 5px,var(--purple) 5px,var(--purple-dark) 147px,#6a4f8a 147px,#6a4f8a 153px)}
  .brand{position:absolute;left:161px;top:52px;display:flex;align-items:center;gap:10px;color:var(--white);font-size:30px;font-weight:600;white-space:nowrap}
  .brand-mark{width:12px;height:12px;background:var(--gold)}
  .header-contacts{position:absolute;right:133px;top:36px;display:flex;gap:12px}
  .contact-pill{height:38px;display:flex;align-items:center;gap:8px;padding:0 14px;white-space:nowrap;
    background:rgba(255,255,255,.06);border:1px solid rgba(0,0,0,.25);border-radius:3px;color:var(--white);font-size:13.5px;letter-spacing:-.2px}
  .main-nav{position:absolute;left:493px;top:97px;width:585px;height:50px;border-top:1px solid rgba(255,255,255,.12);
    display:flex;align-items:center;justify-content:space-between;padding:0 0 0 18px}
  .main-nav a{position:relative;height:49px;display:flex;align-items:center;color:var(--white);font-size:11px;font-weight:700;text-decoration:none;white-space:nowrap}
  .main-nav .sep{width:1px;height:28px;background:rgba(0,0,0,.3)}
  .main-nav a.active::after{content:"";position:absolute;left:0;right:0;bottom:0;height:2px;background:var(--gold)}
  .main-nav a.active::before{content:"";position:absolute;left:50%;bottom:2px;margin-left:-4px;border:4px solid transparent;border-top:0;border-bottom-color:var(--gold)}

  .hero{position:absolute;left:0;top:153px;width:1200px;height:216px;background:linear-gradient(90deg,#d8d8d8,#f0f0f0 40%,#efefef)}
  .hero-photo{position:absolute;left:590px;top:0;width:516px;height:216px;
    background:linear-gradient(100deg,rgba(240,240,240,0) 0,#6d6d6d 12%,#2c2c2c 40%,#8a8a8a 70%,#cfcfcf 88%,rgba(239,239,239,0) 100%)}
  .hero-title{position:absolute;left:155px;top:38px;font-size:33px;font-weight:500;color:var(--purple-text);letter-spacing:-.4px;white-space:nowrap}
  .hero-sub{position:absolute;left:156px;top:82px;font-size:31px;font-weight:500;color:var(--gold);letter-spacing:-.3px}
  .hero-rule{position:absolute;left:156px;top:126px;width:410px;height:2px;background:var(--gold)}
  .hero-text{position:absolute;left:158px;top:139px;width:420px;font-size:15.5px;line-height:25px;color:var(--ink)}

  .contact-card{position:absolute;left:163px;top:393px;width:236px;height:451px;background:#fafafa;box-shadow:0 0 6px rgba(0,0,0,.05)}
  .contact-card h2{position:absolute;left:27px;top:20px;font-size:19px;font-weight:500}
  .contact-card .rule{position:absolute;left:11px;top:47px;width:213px;height:1px;background:var(--gold)}
  .contact-card p{position:absolute;left:24px;top:57px;width:189px;font-size:13px;line-height:16.5px;color:var(--grey);text-align:justify}
  .field{position:absolute;left:18px;width:195px;height:34px;background:var(--white);border:2px solid var(--grey-light);border-radius:3px;font-size:11px;color:#9a9a9a;padding:9px 15px}
  .captcha{position:absolute;left:24px;top:349px;font-size:11px;color:#c9b3e6}
  .send{position:absolute;left:18px;top:394px;width:117px;height:34px;background:var(--gold-soft);color:var(--ink);font-size:14px;font-weight:500;display:flex;align-items:center;justify-content:center}

  .expertise h1{position:absolute;left:436px;top:392px;font-size:27.5px;font-weight:500}
  .expertise .rule{position:absolute;left:430px;top:439px;width:587px;height:1px;background:var(--gold)}
  .expertise ul{list-style:none;position:absolute;left:450px;top:469px}
  .expertise li{position:relative;height:50px;padding-left:27px}
  .expertise li svg{position:absolute;left:1px;top:3px}
  .expertise li strong{display:block;font-size:14px;font-weight:500;color:#555;line-height:17px}
  .expertise li span{display:block;font-size:13px;color:#555;line-height:17px}
  .divider{position:absolute;left:403px;top:1092px;width:586px;height:1px;background:var(--grey-light)}
  .mission{position:absolute;left:438px;top:1114px;font-size:24px;line-height:33px;color:var(--purple-text);font-weight:500}
</style>
</head>
<body>
<div class="page">
  <header class="site-header">
    <div class="brand"><span class="brand-mark"></span>Dunmore Willett</div>
    <div class="header-contacts">
      <div class="contact-pill phone">
        <svg width="15" height="15" viewBox="0 0 16 16"><circle cx="8" cy="8" r="7" fill="none" stroke="#d4b66a" stroke-width="1.4"/><path d="M5.5 4.5l1.5 1.6-.8 1.2c.5 1 1.3 1.8 2.3 2.3l1.2-.8 1.6 1.5-.9 1.1c-2.6-.3-5-2.7-5.2-5.2z" fill="#d4b66a"/></svg>
        0300-555-0142
      </div>
      <div class="contact-pill email">
        <svg width="18" height="13" viewBox="0 0 18 13"><rect x="1" y="1" width="16" height="11" fill="none" stroke="#d4b66a" stroke-width="1.4"/><path d="M1 1l8 6 8-6" fill="none" stroke="#d4b66a" stroke-width="1.4"/></svg>
        daniel@dunmorewillett.example
      </div>
    </div>
    <nav class="main-nav">
      <a>HOME</a><span class="sep"></span>
      <a class="active">AREAS OF EXPERTICE</a><span class="sep"></span>
      <a>DANIEL DUNMORE</a><span class="sep"></span>
      <a>PETER WILLETT</a><span class="sep"></span>
      <a>CONTACT US</a>
    </nav>
  </header>

  <section class="hero">
    <div class="hero-photo" role="img" aria-label="Black and white photograph of classical stone columns and a portico"></div>
    <div class="hero-title">Dunmore Willett Solicitors</div>
    <div class="hero-sub">Areas Of Expertice</div>
    <div class="hero-rule"></div>
    <p class="hero-text">Lorem ipsum dolor sit amet, consectetur adipisicing elit, sed do eiusmod tempor incidi</p>
  </section>

  <aside class="contact-card">
    <h2>Contact Us</h2>
    <div class="rule"></div>
    <p>If you have any quesition, feel free to contact us, we’ll answer your question in time lapse of less than 24 hours.</p>
    <div class="field" style="top:141px">Full Name</div>
    <div class="field" style="top:184px">Phone</div>
    <div class="field" style="top:227px">Email</div>
    <div class="field" style="top:270px;height:58px">Your Message</div>
    <div class="captcha">5 + 2 =</div>
    <div class="field" style="left:69px;top:340px;width:145px">Answer</div>
    <div class="send">SEND</div>
  </aside>

  <section class="expertise">
    <h1>Areas of Expertise</h1>
    <div class="rule"></div>
    <ul>
      <li><svg width="12" height="12" viewBox="0 0 12 12"><circle cx="6" cy="6" r="6" fill="#d4b66a"/><path d="M3.3 6.2l1.8 1.7 3.6-3.6" fill="none" stroke="#fff" stroke-width="1.5"/></svg><strong>Litigation</strong><span>Private and commercial</span></li>
      <li><svg width="12" height="12" viewBox="0 0 12 12"><circle cx="6" cy="6" r="6" fill="#d4b66a"/><path d="M3.3 6.2l1.8 1.7 3.6-3.6" fill="none" stroke="#fff" stroke-width="1.5"/></svg><strong>Company Matters</strong><span>Acquisitions &amp; mergers, financing, share agreements, joint venture agreements</span></li>
      <li><svg width="12" height="12" viewBox="0 0 12 12"><circle cx="6" cy="6" r="6" fill="#d4b66a"/><path d="M3.3 6.2l1.8 1.7 3.6-3.6" fill="none" stroke="#fff" stroke-width="1.5"/></svg><strong>Insolvency</strong><span>Corporate and private</span></li>
      <li><svg width="12" height="12" viewBox="0 0 12 12"><circle cx="6" cy="6" r="6" fill="#d4b66a"/><path d="M3.3 6.2l1.8 1.7 3.6-3.6" fill="none" stroke="#fff" stroke-width="1.5"/></svg><strong>Conveyancing</strong><span>Commercial and Residential</span></li>
      <li><svg width="12" height="12" viewBox="0 0 12 12"><circle cx="6" cy="6" r="6" fill="#d4b66a"/><path d="M3.3 6.2l1.8 1.7 3.6-3.6" fill="none" stroke="#fff" stroke-width="1.5"/></svg><strong>Wills &amp; Probate</strong><span>Estate planning, disputes, administration</span></li>
      <li><svg width="12" height="12" viewBox="0 0 12 12"><circle cx="6" cy="6" r="6" fill="#d4b66a"/><path d="M3.3 6.2l1.8 1.7 3.6-3.6" fill="none" stroke="#fff" stroke-width="1.5"/></svg><strong>Landlord &amp; Tenant</strong><span>Agreements and disputes</span></li>
      <li><svg width="12" height="12" viewBox="0 0 12 12"><circle cx="6" cy="6" r="6" fill="#d4b66a"/><path d="M3.3 6.2l1.8 1.7 3.6-3.6" fill="none" stroke="#fff" stroke-width="1.5"/></svg><strong>Divorce</strong><span>Ancillary relief, children, mediation</span></li>
      <li><svg width="12" height="12" viewBox="0 0 12 12"><circle cx="6" cy="6" r="6" fill="#d4b66a"/><path d="M3.3 6.2l1.8 1.7 3.6-3.6" fill="none" stroke="#fff" stroke-width="1.5"/></svg><strong>Care of the Elderly</strong><span>Powers of Attorney, Court of Protection</span></li>
      <li><svg width="12" height="12" viewBox="0 0 12 12"><circle cx="6" cy="6" r="6" fill="#d4b66a"/><path d="M3.3 6.2l1.8 1.7 3.6-3.6" fill="none" stroke="#fff" stroke-width="1.5"/></svg><strong>Intellectual Property</strong><span>Copyright, patents, designs</span></li>
      <li><svg width="12" height="12" viewBox="0 0 12 12"><circle cx="6" cy="6" r="6" fill="#d4b66a"/><path d="M3.3 6.2l1.8 1.7 3.6-3.6" fill="none" stroke="#fff" stroke-width="1.5"/></svg><strong>Commercial Crime</strong><span>‘White Collar’ crime</span></li>
      <li><svg width="12" height="12" viewBox="0 0 12 12"><circle cx="6" cy="6" r="6" fill="#d4b66a"/><path d="M3.3 6.2l1.8 1.7 3.6-3.6" fill="none" stroke="#fff" stroke-width="1.5"/></svg><strong>Media Law</strong><span>Film, TV, Theatre, Radio</span></li>
      <li><svg width="12" height="12" viewBox="0 0 12 12"><circle cx="6" cy="6" r="6" fill="#d4b66a"/><path d="M3.3 6.2l1.8 1.7 3.6-3.6" fill="none" stroke="#fff" stroke-width="1.5"/></svg><strong>Commercial / Business</strong><span>Structures, agreements, contracts, disputes</span></li>
    </ul>
  </section>

  <div class="divider"></div>
  <p class="mission">Our mission is to help our clients achieve their<br>Legal goals by providing proven legal counseling.</p>
</div>
</body>
</html>
```